Vendro-s / stay-rooted -> Align your thoughts and emotions with world peace

[En español at the end] Very good! Thank you for showing interest in our project :) We need a logo design and web design for a foundation based in Barcelona. Our goal is to work with people's psychology and philosophy to make their lives happier as well as the rest of the world, because we believe we can align them. The name of the foundation is "vendro-s" (véndrose), which comes to say that there is a way to align a series of concepts that take us from the peace and inner happiness of the individual to world peace and happiness. Very much in the line of Orrin Thale's quotation: "All the problems of humanity derive from that we do not know how to remain alone and quiet in a room". The concepts we want to align are the following, and in this order: Inner Peace Practical Philosophy Emotional Intelligence Critical Thinking Social Justice Conflict Resolution World Peace We enclose a couple of possible logo and web ideas, very grotesque and rudimentary. We are sure that you will be able to capture the idea and improve it in such a way that the idea will win with your contribution. Thank you very much in advance! Ah! And, vendro-s :-) -------------- Hi! Thanks for paying attention to this project! We are looking for a logo and web design for an association whose goal is to work with the psychology and philosophy of people in order to make their life happier as well as the happiness of the rest of the world. The name of the organization is "vendro-s" (get aligned) meaning that we can align ourselves with the next concepts (in this order): inner peace - practical philosophy - emotional intelligence - critical thinking - social justice - conflict resolution - global Peace Find some basic ideas that you might find in order to grasp what we are looking for, but feel free to add your own contribution, I am sure you can surprise us! :) Thank you in advance, Get aligned!

Project Deadline Extended Reason: Deadline extension conceded, however, it is highly recommended to have the final design by Tuesday 23rd of May at 5 pm, UTC + 1. Extension of the granted deadline, however, it is highly recommended to have the final design on Tuesday, May 23 at 5:00 p.m. (local Spain). Added Monday, May 22, 2017

Target Market(s)

We addressed mainly middle-class people with concerns for personal development. In the medium term, we plan to cover the spectrum of companies with training courses for their staff. The first project that we are sure will be carried out is the application of critical thinking for adolescents and young people.

Logo Text

Vendr-s

Number of Pages Required

1 page

Font styles to use
Sans Serif

Colors
3176b5
f37122

Requirements
Must have
• The essential elements are relatively abstract and numerous. Those exposed before: Inner Peace, Practical Philosophy, Emotional Intelligence, Critical Thinking, Social Justice, Conflict Resolution, World Peace. Probably the most striking or relevant will be two: emotional intelligence and critical thinking. The next level would be occupied by inner peace through meditation and introspection. And in the last level the other three.
Nice to have
• We want to transmit integrity and transparency, which in turn will be pillars of the educational and philosophical methods that we will teach. Empathy and compassion are also key. We have marked some colors, but still feel free to use another / others in your design. Sure you have great ideas :-) and we are looking forward to seeing them
Should not have
• We want to avoid at all costs the sensation of pseudoscience and volatility. Our values ​​are deep and we prefer to die rather than transmit an ambiguous, wrong, superfluous or interested message (in the sense of chaquetero).

```html
<!DOCTYPE html>
<html lang="es">
<head>
<meta charset="utf-8">
<title>Vendro-s · Tu paz interior y la mundial</title>
<link href="https://fonts.googleapis.com/css2?family=Open+Sans:ital,wght@0,400;0,600;0,700;1,400&family=Oswald:wght@400;500&display=swap" rel="stylesheet">
<style>
:root{
  --brand-blue:#3176b5;
  --brand-orange:#f37122;
  --ink:#2b2b2b;
  --white:#ffffff;
  --footer:#1f1f1f;
  --stage-fill:#2a241c;
  --stage-text:#f1e2b8;
}
*{box-sizing:border-box;margin:0;padding:0}
html,body{width:1200px;height:4180px;overflow:hidden}
body{position:relative;font-family:"Open Sans",Arial,sans-serif;background:var(--white);color:var(--ink)}

.site-header{position:absolute;top:0;left:0;width:1200px;height:100px;background:var(--white)}
.brand{position:absolute;left:234px;top:22px;display:flex;align-items:center;gap:12px}
.brand-dot{width:52px;height:52px;border-radius:50%;background:var(--brand-blue)}
.brand-name{font-weight:700;font-size:38px;color:var(--brand-blue);letter-spacing:.5px}
.main-nav{position:absolute;left:690px;top:42px;display:flex;gap:30px;font-size:13px;color:#555}

.hero{position:absolute;top:100px;left:0;width:1200px;height:292px;overflow:hidden;
  background:radial-gradient(circle at 8% 40%,#b06a2a 0,#3a2414 12%,transparent 26%),
             radial-gradient(circle at 96% 30%,#3f7ec4 0,#1d4a7a 14%,transparent 30%),
             linear-gradient(180deg,#141820,#0b0d12)}
.hero-title{position:absolute;top:14px;width:100%;text-align:center;font-family:"Oswald",Arial,sans-serif;font-size:27px;letter-spacing:4px;color:var(--white);font-weight:500}
.stage-main{position:absolute;left:153px;top:76px;width:160px;height:160px;border-radius:50%;background:var(--white);display:flex;align-items:center;justify-content:center;text-align:center;font-family:"Oswald",Arial,sans-serif;font-size:34px;line-height:1.05;color:#333}
.stage{position:absolute;top:113px;width:86px;height:86px;border-radius:50%;background:var(--stage-fill);display:flex;align-items:center;justify-content:center;text-align:center;font-family:"Oswald",Arial,sans-serif;font-size:12px;line-height:1.15;color:var(--stage-text);padding:6px}

.topic{position:absolute;left:0;width:1200px;overflow:hidden;color:var(--white);text-align:center}
.topic-photo{position:absolute;inset:0}
.topic h2{position:relative;margin-top:28px;font-size:32px;font-weight:700;text-shadow:0 1px 4px rgba(0,0,0,.5)}
.topic .lead{position:relative;width:560px;margin:6px auto 0;font-size:10.5px;line-height:1.3;text-shadow:0 1px 2px rgba(0,0,0,.6)}
.topic p.body{position:relative;width:620px;margin:60px auto 0;font-size:14px;font-style:italic;line-height:1.38;text-shadow:0 1px 3px rgba(0,0,0,.6)}
.topic p.body + p.body{margin-top:22px}

.t1{top:392px;height:501px}
.t2{top:893px;height:500px}
.t3{top:1393px;height:498px}
.t4{top:1891px;height:503px}
.t5{top:2394px;height:497px}
.t6{top:2891px;height:501px}
.t7{top:3392px;height:503px}

.t1 .topic-photo{background:linear-gradient(100deg,#1f5f9e 0%,#4f95c7 30%,#9cc3a4 55%,#8fb07a 75%,#c9a94a 100%)}
.t2 .topic-photo{background:linear-gradient(180deg,#6d6e70 0%,#3c3d3f 45%,#4a4038 80%,#2a2622 100%)}
.t3 .topic-photo{background:linear-gradient(180deg,#d78a3e 0%,#b07a52 40%,#6c5a4e 75%,#3e3a3a 100%)}
.t4 .topic-photo{background:radial-gradient(circle at 50% 55%,#5d6a55 0,#384236 45%,#1f241e 100%)}
.t5 .topic-photo{background:linear-gradient(180deg,#7f8890 0%,#a4a8aa 50%,#5a5753 100%)}
.t6 .topic-photo{background:linear-gradient(180deg,#2f78b8 0%,#6ba2cf 45%,#b98a6a 80%,#8a5b3e 100%)}
.t7 .topic-photo{background:radial-gradient(circle at 60% 40%,#d9ddb0 0,#7fae3a 30%,#3d7a1e 70%,#1e4a10 100%)}

.timeline{position:absolute;left:980px;top:370px;width:3px;height:3502px;background:var(--brand-orange)}
.marker{position:absolute;left:972px;width:19px;height:19px;border-radius:50%;background:var(--brand-blue);border:2px solid #cfe1f2}

.site-footer{position:absolute;top:3895px;left:0;width:1200px;height:285px;background:var(--footer);color:#aaa;text-align:center}
.site-footer .brand{position:static;justify-content:center;margin-top:55px}
.site-footer .brand-dot{width:44px;height:44px}
.site-footer .brand-name{font-size:32px}
.footer-nav{display:flex;justify-content:center;gap:30px;font-size:13px;margin-top:18px}
.social{display:flex;justify-content:center;gap:22px;margin-top:30px;font-size:14px;font-weight:600;color:var(--brand-blue)}
.footer-rule{position:absolute;left:578px;bottom:10px;width:44px;height:2px;background:#666}
</style>
</head>
<body>

<header class="site-header">
  <div class="brand"><span class="brand-dot"></span><span class="brand-name">vendro-s</span></div>
  <nav class="main-nav"><span>Inicio</span><span>Filosofía</span><span>participar</span><span>contacto</span></nav>
</header>

<section class="hero" role="img" aria-label="Fondo: espacio con planeta y luz cálida; conceptos alineados en fila">
  <h1 class="hero-title">VENDRO-S: TU PAZ INTERIOR Y LA MUNDIAL</h1>
  <div class="stage-main">PAZ<br>INTERIOR</div>
  <div class="stage" style="left:368px">FILOSOFÍA PRÁCTICA</div>
  <div class="stage" style="left:474px">INTELIGENCIA EMOCIONAL</div>
  <div class="stage" style="left:582px">PENSAMIENTO CRÍTICO</div>
  <div class="stage" style="left:702px">RESOLUCIÓN CONFLICTOS</div>
  <div class="stage" style="left:810px">JUSTICIA SOCIAL</div>
  <div class="stage" style="left:924px">PAZ MUNDIAL</div>
</section>

<section class="topic t1">
  <div class="topic-photo" role="img" aria-label="Foto: persona meditando junto al agua en calma"></div>
  <h2>Paz interior</h2>
  <p class="lead">Un camino sereno hacia el equilibrio personal, donde cada pensamiento encuentra su lugar y cada emoción se escucha con calma y respeto.</p>
  <p class="body">Proponemos talleres y encuentros abiertos para personas que desean conocerse mejor. Trabajamos con métodos claros, probados y honestos, lejos de promesas vacías. Cada sesión combina reflexión, diálogo y práctica guiada, para que lo aprendido pase de la idea a la vida diaria y se comparta con quienes nos rodean.</p>
  <p class="body">Creemos que la paz empieza dentro de cada uno y se extiende hacia la familia, la escuela, el trabajo y la comunidad. Por eso acompañamos procesos reales, con empatía y compasión, midiendo resultados y revisando lo que hacemos con total transparencia.</p>
</section>

<section class="topic t2">
  <div class="topic-photo" role="img" aria-label="Foto: vías de tren que se bifurcan hacia dos destinos"></div>
  <h2>Filosofía Práctica</h2>
  <p class="lead">Un camino sereno hacia el equilibrio personal, donde cada pensamiento encuentra su lugar y cada emoción se escucha con calma y respeto.</p>
  <p class="body">Proponemos talleres y encuentros abiertos para personas que desean conocerse mejor. Trabajamos con métodos claros, probados y honestos, lejos de promesas vacías. Cada sesión combina reflexión, diálogo y práctica guiada, para que lo aprendido pase de la idea a la vida diaria y se comparta con quienes nos rodean.</p>
  <p class="body">Creemos que la paz empieza dentro de cada uno y se extiende hacia la familia, la escuela, el trabajo y la comunidad. Por eso acompañamos procesos reales, con empatía y compasión, midiendo resultados y revisando lo que hacemos con total transparencia.</p>
</section>

<section class="topic t3">
  <div class="topic-photo" role="img" aria-label="Ilustración: corazón y cerebro sobre un paisaje al atardecer"></div>
  <h2>Inteligencia emocional</h2>
  <p class="lead">Un camino sereno hacia el equilibrio personal, donde cada pensamiento encuentra su lugar y cada emoción se escucha con calma y respeto.</p>
  <p class="body">Proponemos talleres y encuentros abiertos para personas que desean conocerse mejor. Trabajamos con métodos claros, probados y honestos, lejos de promesas vacías. Cada sesión combina reflexión, diálogo y práctica guiada, para que lo aprendido pase de la idea a la vida diaria y se comparta con quienes nos rodean.</p>
  <p class="body">Creemos que la paz empieza dentro de cada uno y se extiende hacia la familia, la escuela, el trabajo y la comunidad. Por eso acompañamos procesos reales, con empatía y compasión, midiendo resultados y revisando lo que hacemos con total transparencia.</p>
</section>

<section class="topic t4">
  <div class="topic-photo" role="img" aria-label="Foto: laberinto circular visto desde arriba"></div>
  <h2>Pensamiento crítico</h2>
  <p class="lead">Un camino sereno hacia el equilibrio personal, donde cada pensamiento encuentra su lugar y cada emoción se escucha con calma y respeto.</p>
  <p class="body">Proponemos talleres y encuentros abiertos para personas que desean conocerse mejor. Trabajamos con métodos claros, probados y honestos, lejos de promesas vacías. Cada sesión combina reflexión, diálogo y práctica guiada, para que lo aprendido pase de la idea a la vida diaria y se comparta con quienes nos rodean.</p>
  <p class="body">Creemos que la paz empieza dentro de cada uno y se extiende hacia la familia, la escuela, el trabajo y la comunidad. Por eso acompañamos procesos reales, con empatía y compasión, midiendo resultados y revisando lo que hacemos con total transparencia.</p>
</section>

<section class="topic t5">
  <div class="topic-photo" role="img" aria-label="Foto: piezas de ajedrez y fichas de dominó enfrentadas"></div>
  <h2>Resolución conflictos</h2>
  <p class="lead">Un camino sereno hacia el equilibrio personal, donde cada pensamiento encuentra su lugar y cada emoción se escucha con calma y respeto.</p>
  <p class="body">Proponemos talleres y encuentros abiertos para personas que desean conocerse mejor. Trabajamos con métodos claros, probados y honestos, lejos de promesas vacías. Cada sesión combina reflexión, diálogo y práctica guiada, para que lo aprendido pase de la idea a la vida diaria y se comparta con quienes nos rodean.</p>
  <p class="body">Creemos que la paz empieza dentro de cada uno y se extiende hacia la familia, la escuela, el trabajo y la comunidad. Por eso acompañamos procesos reales, con empatía y compasión, midiendo resultados y revisando lo que hacemos con total transparencia.</p>
</section>

<section class="topic t6">
  <div class="topic-photo" role="img" aria-label="Foto: muchas manos alzadas bajo un cielo azul"></div>
  <h2>Justicia social</h2>
  <p class="lead">Un camino sereno hacia el equilibrio personal, donde cada pensamiento encuentra su lugar y cada emoción se escucha con calma y respeto.</p>
  <p class="body">Proponemos talleres y encuentros abiertos para personas que desean conocerse mejor. Trabajamos con métodos claros, probados y honestos, lejos de promesas vacías. Cada sesión combina reflexión, diálogo y práctica guiada, para que lo aprendido pase de la idea a la vida diaria y se comparta con quienes nos rodean.</p>
  <p class="body">Creemos que la paz empieza dentro de cada uno y se extiende hacia la familia, la escuela, el trabajo y la comunidad. Por eso acompañamos procesos reales, con empatía y compasión, midiendo resultados y revisando lo que hacemos con total transparencia.</p>
</section>

<section class="topic t7">
  <div class="topic-photo" role="img" aria-label="Foto: manos sosteniendo el planeta entre hojas verdes"></div>
  <h2>Paz mundial</h2>
  <p class="lead">Un camino sereno hacia el equilibrio personal, donde cada pensamiento encuentra su lugar y cada emoción se escucha con calma y respeto.</p>
  <p class="body">Proponemos talleres y encuentros abiertos para personas que desean conocerse mejor. Trabajamos con métodos claros, probados y honestos, lejos de promesas vacías. Cada sesión combina reflexión, diálogo y práctica guiada, para que lo aprendido pase de la idea a la vida diaria y se comparta con quienes nos rodean.</p>
  <p class="body">Creemos que la paz empieza dentro de cada uno y se extiende hacia la familia, la escuela, el trabajo y la comunidad. Por eso acompañamos procesos reales, con empatía y compasión, midiendo resultados y revisando lo que hacemos con total transparencia.</p>
</section>

<div class="timeline"></div>
<span class="marker" style="top:360px"></span>
<span class="marker" style="top:866px"></span>
<span class="marker" style="top:1366px"></span>
<span class="marker" style="top:1852px"></span>
<span class="marker" style="top:2355px"></span>
<span class="marker" style="top:2861px"></span>
<span class="marker" style="top:3365px"></span>
<span class="marker" style="top:3862px"></span>

<footer class="site-footer">
  <div class="brand"><span class="brand-dot"></span><span class="brand-name">vendro-s</span></div>
  <nav class="footer-nav"><span>Inicio</span><span>Filosofía</span><span>participar</span><span>contacto</span></nav>
  <div class="social" aria-label="Redes sociales"><span>Linkra</span><span>Vidmo</span><span>Pinbo</span><span>Facera</span><span>Chirpa</span><span>Gloop</span></div>
  <div class="footer-rule"></div>
</footer>

</body>
</html>
```